Voltarra: Electrical Contractor flyer design.

We are looking for a sharp and professional flyer to promote the business's cost for specific jobs and to promote the business.
We are a small electrical business looking to break into the market.
Attached logo to be used and following content to be incorporated. Contact details will be given upon final flyer design.

Internal Power Points: $ 120
External Weather Proof Power Points: $150
T.V. Points: $120 (excludes aerial)
T.V. Mounting: $ 200 (Exclude Leads)
Aerials Starting From: $220 Incudes Mast
LED Down lights: $60 per unti
Ceiling Fans: $150 (Fan Excluded)
Oven & Range Hood Change Overs: $250
A.C. Install: $300
S/B Upgrade: From $600
Safety Switch Installation: $280
Phone Points: $120

Services Incude:

New home wiring
Shop & Office Fit Outs
Re - Wires
Extentions
Garden Lighting
Home Thearters
Home Automation
Power Points
Phone, Data
Feature Lighting
Lighting design and Installation
Ceiling Fans
A.C Installation
Oven & Range hood Installation

*All prices are gst inclusive
**Prices subject to change due to site access.

```html
<!DOCTYPE html>
<html lang="en">
<head>
<meta charset="utf-8">
<title>Voltarra – Electrical Contractor Flyer</title>
<link href="https://fonts.googleapis.com/css2?family=Archivo+Black&family=Lato:wght@300;400;700;900&display=swap" rel="stylesheet">
<style>
:root{
  --orange:#e0631f;
  --orange-deep:#c24a12;
  --orange-light:#f08a3c;
  --charcoal:#3b3b3d;
  --ink:#2b2b2b;
  --paper:#ffffff;
  --backdrop:#3a3a3a;
}
*{box-sizing:border-box;margin:0;padding:0}
html,body{width:907px;height:1200px;overflow:hidden;background:var(--backdrop)}
body{font-family:"Lato",sans-serif;position:relative}
.flyer{position:absolute;left:80px;top:75px;width:747px;height:1050px;background:linear-gradient(180deg,#f4f4f4 0%,#e9e9e9 60%,#f3f3f3 100%);overflow:hidden}
.hero-photo{position:absolute;left:0;top:0;width:747px;height:355px;background:radial-gradient(circle at 22% 20%,#f7e7c8 0%,#c9965c 25%,#7a4a2a 55%,#3e2416 100%)}
.shapes{position:absolute;left:0;top:0}
.brand{position:absolute;left:485px;top:300px;display:flex;align-items:center;gap:12px}
.brand-mark{width:22px;height:22px;background:var(--orange)}
.brand-name{font-weight:900;font-size:42px;color:var(--charcoal);letter-spacing:1px}
.headline{position:absolute;left:32px;top:402px;line-height:1}
.headline .domestic{font-family:"Archivo Black",sans-serif;font-size:38px;color:var(--orange);letter-spacing:1px}
.headline .commercial{font-family:"Archivo Black",sans-serif;font-size:30px;color:var(--ink);margin-top:8px}
.headline .company{font-weight:300;font-size:24px;color:var(--ink);letter-spacing:1px;margin-top:6px}
.services-tag{position:absolute;left:0;top:522px;width:225px;height:31px;background:var(--charcoal);color:#fff;font-weight:700;font-size:16px;letter-spacing:.5px;padding:6px 0 0 33px}
.service-list{position:absolute;list-style:none;font-weight:700;font-size:14px;color:var(--ink)}
.service-list li{position:relative;padding-left:17px;height:20.6px;line-height:20.6px}
.service-list li::before{content:"";position:absolute;left:0;top:7px;width:8px;height:8px;background:var(--orange)}
.col-a{left:37px;top:576px}
.col-b{left:227px;top:579px;width:160px}
.col-b li.wrap{height:auto;line-height:19px}
.col-b li.wrap::before{top:6px}
.cta{position:absolute;left:27px;top:778px;font-family:"Archivo Black",sans-serif;font-size:33px;color:var(--orange);text-shadow:2px 2px 0 rgba(0,0,0,.25);letter-spacing:.5px}
.contacts{position:absolute;left:31px;top:829px;font-family:"Archivo Black",sans-serif;font-size:18px;color:var(--charcoal);line-height:23px;letter-spacing:.6px}
.contacts .who{color:var(--orange);font-family:"Lato",sans-serif;font-weight:900;font-size:18px;letter-spacing:0}
.footer-links{position:absolute;left:36px;top:932px;list-style:none;color:#fff;font-weight:700;font-size:14.5px}
.footer-links li{display:flex;align-items:center;gap:11px;height:24.5px}
.footer-links svg{flex:none}
.price-list{position:absolute;left:425px;top:436px;width:292px;color:#fff;list-style:none}
.price-list li{margin-bottom:3px}
.price-row{display:flex;align-items:baseline;font-size:12px;font-weight:700;line-height:18px}
.price-row .label{white-space:nowrap}
.price-row .dots{flex:1;border-bottom:2px dotted rgba(255,255,255,.85);margin:0 2px 3px}
.price-row .amount{font-size:16px;font-weight:900;white-space:nowrap}
.price-note{font-size:12px;font-weight:700;line-height:14px}
.gst-notes{position:absolute;left:425px;top:798px;width:292px;color:#fff;font-size:11px;font-weight:700;line-height:15px}
.spot{position:absolute;top:850px;width:127px;height:137px;border:2px solid #fff}
.spot-house{left:436px;background:linear-gradient(180deg,#0d0f16 0%,#1c1c22 55%,#5a4a30 75%,#222 100%)}
.spot-bulb{left:582px;background:radial-gradient(circle at 50% 55%,#fff7e8 0%,#f2b37a 18%,#b0502a 42%,#2a0f08 80%)}
</style>
</head>
<body>
<main class="flyer">
  <div class="hero-photo" role="img" aria-label="Elegant living room with chandelier, curtains, fireplace and warm lamps"></div>

  <svg class="shapes" width="747" height="1050" viewBox="0 0 747 1050" aria-hidden="true">
    <defs>
      <linearGradient id="panelShade" x1="0" y1="0" x2="1" y2="1">
        <stop offset="0" stop-color="#f08a3c" stop-opacity=".5"/>
        <stop offset="1" stop-color="#b8440f" stop-opacity=".6"/>
      </linearGradient>
    </defs>
    <rect x="414" y="410" width="333" height="640" fill="var(--orange)"/>
    <rect x="414" y="410" width="333" height="640" fill="url(#panelShade)"/>
    <rect x="0" y="347" width="400" height="4" fill="var(--orange)"/>
    <rect x="0" y="355" width="395" height="12" fill="var(--charcoal)"/>
    <path d="M440 226 H747 V420 H470 Q446 420 432 398 L392 333 Q383 318 392 302 L414 250 Q424 226 440 226 Z" fill="var(--charcoal)"/>
    <path d="M448 238 H747 V408 H476 Q456 408 444 390 L406 330 Q399 318 406 305 L428 258 Q436 238 448 238 Z" fill="var(--orange)"/>
    <path d="M456 246 H747 V398 H482 Q464 398 454 382 L418 326 Q413 318 418 308 L438 264 Q445 246 456 246 Z" fill="var(--paper)"/>
    <path d="M0 895 H360 Q395 895 405 920 L414 940 V1050 H0 Z" fill="var(--orange)"/>
    <path d="M0 903 H356 Q388 903 398 926 L414 958 V1050 H0 Z" fill="var(--charcoal)"/>
  </svg>

  <div class="brand">
    <span class="brand-mark"></span>
    <span class="brand-name">Voltarra</span>
  </div>

  <div class="headline">
    <div class="domestic">DOMESTIC</div>
    <div class="commercial">&amp;COMMERCIAL</div>
    <div class="company">ELECTRICAL COMPANY</div>
  </div>

  <div class="services-tag">Services Incude</div>
  <ul class="service-list col-a">
    <li>Shop &amp; office fit-outs</li>
    <li>Re-wires</li>
    <li>Garden lighting</li>
    <li>Home theatres</li>
    <li>Home automation</li>
    <li>Power points</li>
    <li>Phone &amp; data</li>
    <li>Feature lighting</li>
    <li>Lighting design &amp; installation</li>
  </ul>
  <ul class="service-list col-b">
    <li>Ceiling fans</li>
    <li>AC installation</li>
    <li class="wrap">Oven &amp; rangehood installation</li>
  </ul>

  <div class="cta">Call us now</div>
  <div class="contacts">
    <div><span class="who">Reid</span> - 0400118245</div>
    <div><span class="who">Callum</span> - 0400572903</div>
  </div>

  <ul class="footer-links">
    <li><svg width="15" height="15" viewBox="0 0 16 16"><circle cx="8" cy="8" r="7" fill="none" stroke="var(--orange)" stroke-width="1.8"/><path d="M1 8H15M8 1V15M3 4H13M3 12H13" stroke="var(--orange)" stroke-width="1.2"/></svg>www.voltarra.com</li>
    <li><svg width="15" height="15" viewBox="0 0 16 16"><rect x="1" y="3" width="14" height="10" fill="var(--orange)"/><path d="M1 3L8 9L15 3" fill="none" stroke="var(--charcoal)" stroke-width="1.4"/></svg>hello@voltarra.com</li>
    <li><svg width="15" height="15" viewBox="0 0 16 16"><rect x="1" y="1" width="14" height="14" fill="var(--orange)"/></svg>www.voltarra.com/community</li>
  </ul>

  <ul class="price-list">
    <li><div class="price-row"><span class="label">Internal power points</span><span class="dots"></span><span class="amount">$120</span></div></li>
    <li><div class="price-note">External weather proof</div>
        <div class="price-row"><span class="label">Powerpoints</span><span class="dots"></span><span class="amount">$150</span></div></li>
    <li><div class="price-row"><span class="label">TV points</span><span class="dots"></span><span class="amount">$120</span></div><div class="price-note">(excludes aerial)</div></li>
    <li><div class="price-row"><span class="label">TV mounting</span><span class="dots"></span><span class="amount">$ 200</span></div><div class="price-note">(Exclude Leads)</div></li>
    <li><div class="price-row"><span class="label">Aerials starting from</span><span class="dots"></span><span class="amount">$ 220</span></div><div class="price-note">Incude Mast</div></li>
    <li><div class="price-row"><span class="label">LED down lights</span><span class="dots"></span><span class="amount">$ 60</span></div><div class="price-note">per unti</div></li>
    <li><div class="price-row"><span class="label">Ceiling fans</span><span class="dots"></span><span class="amount">$ 150</span></div><div class="price-note">(Fan Excluded)</div></li>
    <li><div class="price-row"><span class="label">Oven &amp; range hood change overs</span><span class="dots"></span><span class="amount">$ 250</span></div></li>
    <li><div class="price-row"><span class="label">AC install</span><span class="dots"></span><span class="amount">$ 300</span></div></li>
    <li><div class="price-row"><span class="label">S/B upgrade from</span><span class="dots"></span><span class="amount">$ 600</span></div></li>
    <li><div class="price-row"><span class="label">Safety switch installation</span><span class="dots"></span><span class="amount">$ 280</span></div></li>
    <li><div class="price-row"><span class="label">Phone points</span><span class="dots"></span><span class="amount">$ 120</span></div></li>
  </ul>
  <div class="gst-notes">
    <div>*All prices are GST inclusive</div>
    <div>**Prices subject to change due to site access</div>
  </div>

  <div class="spot spot-house" role="img" aria-label="Modern house exterior lit at night with garden lighting"></div>
  <div class="spot spot-bulb" role="img" aria-label="Glowing energy-saving light bulb cupped in hands"></div>
</main>
</body>
</html>
```